Solo Law Practice Website Design

I am starting a solo law practice that will specialize in criminal defense and family law.

I have a rudimentary understanding of Wordpress as used through the tidalnest web services. The winning design would be compatible with this system so that I can modify content on my own.

I have supplied the written content and the components that I am looking for at the domain name: morganvaleslaw.com.

I would like to take that content and work it into a website that looks more professional and inviting. The two most important goals of the website are ease of navigation and rich content for search engine spiders (for example, integrating articles into pages rather than linking to a word document).

The winning design should be turnkey for me to upload immediately.
Updates

Reason: I will be traveling.

Target Market(s)

Individuals looking for legal services.

Industry/Entity Type

Defense

Requirements
Must have
• My picture should appear at least once in the site.

The design should allow a space for me to post blog or legal updates. Additionally, there should be functionality for me to add additional articles to the site.
Nice to have
• Appropriate pictures for a legal website to break-up text on pages.

Simple flash features that won't significantly slow loading times.

Widgets that drive traffic to a contact page or function.

```html
<!DOCTYPE html>
<html lang="en">
<head>
<meta charset="utf-8">
<title>Law Offices of Morgan Vales PLLC</title>
<link rel="stylesheet" href="https://fonts.googleapis.com/css2?family=Cinzel:wght@400;600&family=Open+Sans:wght@400;600;700&family=Noto+Serif:ital@1&display=swap">
<style>
:root{
  --header-top:#6b625d;
  --header-bottom:#3f3834;
  --nav-bg:#2f2a27;
  --page-bg:#ecebdc;
  --card-bg:#ffffff;
  --card-border:#dcdbcb;
  --accent:#a2461c;
  --accent-gold:#e6a83a;
  --text:#4a4542;
  --muted:#6f6a66;
  --footer-bg:#4a4340;
  --footer-panel:#3a3431;
  --footer-text:#d8d2cc;
  --bottom-bar:#2e2926;
  --field-border:#cfcfc6;
}
*{box-sizing:border-box;margin:0;padding:0}
html,body{width:794px;height:1200px;overflow:hidden}
body{position:relative;background:var(--page-bg);font-family:"Open Sans",Arial,sans-serif;color:var(--text)}
.abs{position:absolute}

.site-header{left:0;top:0;width:794px;height:124px;background:radial-gradient(ellipse at 50% 0,#7a716b 0,var(--header-top) 35%,var(--header-bottom) 100%)}
.brand-mark{left:365px;top:17px;width:62px;height:62px;border-radius:50%;background:#3a3330;border:2px solid #5c534e}
.brand-name{left:0;top:84px;width:794px;text-align:center;font-family:"Cinzel",serif;font-size:19px;color:#f3efe9;letter-spacing:.5px}

.main-nav{left:0;top:124px;width:794px;height:29px;background:var(--nav-bg);border-bottom:1px solid #1f1b19;display:flex;justify-content:center;gap:15px;align-items:center;font-size:9px;font-weight:700}
.main-nav a{color:#f1ede8;text-decoration:none}
.main-nav a.active{color:var(--accent-gold)}

.hero{left:93px;top:158px;width:604px;height:199px;background:#fff;border:1px solid #d6d5c6;padding:4px}
.hero-image{width:594px;height:189px;background:linear-gradient(90deg,#8a7464 0,#a86a3e 35%,#b9541c 55%,#8d3a12 100%)}
.hero-title{left:368px;top:195px;width:290px;font-family:"Cinzel",serif;font-weight:600;font-size:21px;line-height:25px;color:#fff}
.hero-sub{left:370px;top:267px;width:275px;font-style:italic;font-size:13px;line-height:17px;color:#f5c89a}
.hero-arrow{width:34px;height:40px;background:#fff;top:238px;display:flex;align-items:center;justify-content:center}
.hero-arrow.prev{left:97px;width:18px;border-radius:0 20px 20px 0}
.hero-arrow.next{left:672px;width:20px;border-radius:20px 0 0 20px}
.hero-pager{left:570px;top:334px;width:100px;height:18px;background:#fff;border-radius:8px 8px 0 0;display:flex;gap:3px;justify-content:center;align-items:center}
.hero-pager i{width:7px;height:7px;border-radius:50%;background:#cfcfcf;border:1px solid #aaa}
.hero-pager i.on{background:#555}

.welcome-title{left:93px;top:373px;font-family:"Cinzel",serif;font-weight:400;font-size:16.5px;color:var(--accent)}
.welcome-text{left:94px;top:403px;width:436px;font-size:10px;line-height:14.2px}
.read-more{font-family:"Noto Serif",serif;font-style:italic;font-size:8.5px;color:var(--muted)}
.welcome-more{left:483px;top:483px}
.divider{left:93px;top:506px;width:432px;height:2px;background:#d8d7c6}

.section-title{left:92px;font-family:"Cinzel",serif;font-weight:400;font-size:13.5px;color:#3d3835}
.practice-card{left:93px;width:432px;height:115px;background:var(--card-bg);border:1px solid var(--card-border)}
.practice-thumb{position:absolute;left:9px;top:9px;width:118px;height:93px;border:3px solid #d4d4d4;background:#eee}
.practice-thumb div{width:100%;height:100%}
.practice-copy{position:absolute;left:137px;top:7px;width:288px;font-size:9.3px;line-height:14px;color:var(--muted)}
.practice-copy p+p{margin-top:13px}
.practice-card .read-more{position:absolute;right:11px;top:92px}

.widget{left:560px;width:136px;background:#fff;border:1px solid var(--card-border);padding:6px 7px}
.widget h3{font-size:9px;font-weight:600;letter-spacing:.6px;color:#3d3835;padding-bottom:6px;border-bottom:1px dotted #c9c9c0;margin-bottom:9px}
.field{height:21px;border:2px solid var(--field-border);font-family:"Noto Serif",serif;font-style:italic;font-size:8px;color:#777;padding:4px 4px;margin-bottom:10px;background:#fff}
.search-field{background:#ececec;border:none;display:flex;justify-content:space-between}
.form-label{font-size:8px;margin:-4px 0 4px}
.field.select{display:flex;justify-content:space-between}
.field.area{height:90px}
.submit-btn{width:60px;height:18px;border-radius:9px;background:linear-gradient(#fafafa,#d8d8d8);border:1px solid #b8b8b8;font-family:"Noto Serif",serif;font-style:italic;font-weight:700;font-size:9px;color:#333;text-align:center;line-height:16px;margin-top:-2px}

.newsletter{left:560px;top:751px;width:134px;height:129px;background:#fff;border:1px solid var(--card-border);padding:4px 11px}
.newsletter h3{font-family:"Cinzel",serif;font-size:11.5px;letter-spacing:.5px;color:#3d3835;border-bottom:1px solid #ddd;padding-bottom:2px}
.newsletter p{font-size:7.8px;line-height:12px;margin-top:4px}
.newsletter .field{height:17px;border:1px solid var(--field-border);font-family:"Open Sans",sans-serif;font-style:normal;font-size:7.5px;color:#333;padding:3px 4px;margin:4px 0 5px}
.signup{display:inline-block;background:var(--accent-gold);color:#fff;font-size:8.5px;padding:3px 6px}
.envelope{position:absolute;right:6px;bottom:6px;width:36px;height:24px;background:linear-gradient(#f6f6f6,#dedede);transform:rotate(-12deg)}

.site-footer{left:0;top:996px;width:794px;height:167px;background:linear-gradient(#554d49,var(--footer-bg))}
.contact-panel{left:93px;top:1015px;width:430px;height:126px;background:var(--footer-panel)}
.contact-panel h4{position:absolute;left:15px;top:12px;font-family:"Cinzel",serif;font-weight:400;font-size:10px;color:#d98b3a;letter-spacing:.5px}
.contact-panel .lead{position:absolute;left:15px;top:37px;font-size:8px;font-weight:700;color:#fff}
.contact-panel .note{position:absolute;left:15px;width:325px;font-size:7.3px;line-height:11.5px;color:var(--footer-text)}
.contact-panel .note.single{white-space:nowrap}
.contact-panel a{color:var(--accent-gold);text-decoration:none}
.attorney-photo{position:absolute;left:342px;top:-12px;width:88px;height:138px;background:linear-gradient(#3f3936,#2a2523)}
.talk-badge{left:565px;top:997px;width:124px;height:50px;background:linear-gradient(#d89a3c,#b1701f);border-radius:0 0 6px 6px;text-align:center;color:#fff}
.talk-badge .name{font-size:14px;font-weight:700;margin-top:7px}
.talk-badge .num{font-size:11px;margin-top:1px;letter-spacing:.5px}
.social{top:1108px;font-size:8px;color:var(--footer-text);display:flex;align-items:center;gap:5px}
.social i{width:11px;height:11px;background:#7e7670;display:block}
.copyright{left:541px;top:1131px;font-size:7.5px;color:#fff}
.bottom-nav{left:0;top:1163px;width:794px;height:37px;background:var(--bottom-bar);display:flex;justify-content:center;align-items:flex-start;padding-top:9px;font-size:7.3px;font-weight:600;letter-spacing:.2px}
.bottom-nav a{color:#cfc8c2;text-decoration:none;padding:2px 7px;border-left:1px solid #46403c}
.bottom-nav a:first-child{border-left:none}
</style>
</head>
<body>

<header class="site-header abs">
  <div class="brand-mark abs"></div>
  <div class="brand-name abs">Law Offices of Morgan Vales PLLC</div>
</header>

<nav class="main-nav abs">
  <a class="active" href="#">Criminal Law</a><a href="#">Family Law</a><a href="#">Will Drafting</a><a href="#">Attorney Profile</a><a href="#">Fees</a><a href="#">Legal Updates</a><a href="#">Online Resources</a><a href="#">Articles</a><a href="#">Contact</a>
</nav>

<section class="hero abs">
  <div class="hero-image" role="img" aria-label="Attorney reviewing documents with two clients, gavel in background"></div>
</section>
<div class="hero-title abs">Lorem is simply dummy text of the printing...</div>
<div class="hero-sub abs">Neque porro quisquam est qui dolorem ipsum quia dolor sit amet.</div>
<div class="hero-arrow prev abs"><svg width="8" height="10"><path d="M6 1 2 5l4 4" fill="none" stroke="#888" stroke-width="1.5"/></svg></div>
<div class="hero-arrow next abs"><svg width="8" height="10"><path d="M2 1l4 4-4 4" fill="none" stroke="#888" stroke-width="1.5"/></svg></div>
<div class="hero-pager abs"><i></i><i></i><i class="on"></i><i></i><i></i><i></i></div>

<h1 class="welcome-title abs">Welcome to Law Offices of Morgan Vales PLLC</h1>
<p class="welcome-text abs">About Me.&nbsp; My practice is focused on accomplishing your goals through results-oriented work at a discount price.&nbsp; For your convenience, I handle legal matters throughout the Twin Cities, including Hennepin, Ramsey, Anoka, and Washington counties.&nbsp; I understand that legal issues can appear complicated, and that is why I take a hands-on approach to guiding you through your legal needs.</p>
<span class="read-more welcome-more abs">Read More...</span>
<div class="divider abs"></div>

<h2 class="section-title abs" style="top:523px">Criminal Law</h2>
<article class="practice-card abs" style="top:547px">
  <div class="practice-thumb"><div role="img" aria-label="Handcuffed hands beside a judge's gavel" style="background:linear-gradient(135deg,#e4ddd6,#8a4a2c)"></div></div>
  <div class="practice-copy"><p>Nulla nec ante sit amet felis gravida tincidunt et non mi. Ut accumsan hep sollicitudin neque sit amet ullamcorper.</p><p>Quisque viverra sem id quamir imperdiet et dictum metus scelerisque. Fusce pellentesque vulputate nisl semper...</p></div>
  <span class="read-more">Read More...</span>
</article>

<h2 class="section-title abs" style="top:671px">Family Law</h2>
<article class="practice-card abs" style="top:695px">
  <div class="practice-thumb"><div role="img" aria-label="Couple meeting with an advisor" style="background:linear-gradient(135deg,#5a4a40,#d9c7b6)"></div></div>
  <div class="practice-copy"><p>Nulla nec ante sit amet felis gravida tincidunt et non mi. Ut accumsan hep sollicitudin neque sit amet ullamcorper.</p><p>Quisque viverra sem id quamir imperdiet et dictum metus scelerisque. Fusce pellentesque vulputate nisl semper...</p></div>
  <span class="read-more">Read More...</span>
</article>

<h2 class="section-title abs" style="top:819px">Will Drafting</h2>
<article class="practice-card abs" style="top:843px">
  <div class="practice-thumb"><div role="img" aria-label="Last will and testament document with a pen and calculator" style="background:linear-gradient(135deg,#c9ccd2,#eef0f3)"></div></div>
  <div class="practice-copy"><p>Nulla nec ante sit amet felis gravida tincidunt et non mi. Ut accumsan hep sollicitudin neque sit amet ullamcorper.</p><p>Quisque viverra sem id quamir imperdiet et dictum metus scelerisque. Fusce pellentesque vulputate nisl semper...</p></div>
  <span class="read-more">Read More...</span>
</article>

<aside>
  <div class="widget abs" style="top:369px;height:60px">
    <h3>SEARCH</h3>
    <div class="field search-field"><span>Search here...</span><svg width="9" height="9"><circle cx="3.5" cy="3.5" r="2.6" fill="none" stroke="#222" stroke-width="1.4"/><path d="M5.5 5.5 8.5 8.5" stroke="#222" stroke-width="1.6"/></svg></div>
  </div>
  <div class="widget abs" style="top:441px;height:297px">
    <h3>CONTACT FORM</h3>
    <div class="field">Name:</div>
    <div class="field">Email:</div>
    <div class="field">Phone:</div>
    <div class="form-label">Preferred Contact Method</div>
    <div class="field select"><span>Phone:</span><svg width="7" height="5"><path d="M0 0h7L3.5 4z" fill="#999"/></svg></div>
    <div class="field area">Describe your legal issue:</div>
    <div class="submit-btn">Submit »</div>
  </div>
  <div class="newsletter abs">
    <h3>Newsletter</h3>
    <p>Enter your email address to receive notifications of legal updates by e-mail</p>
    <div class="field">Email Address</div>
    <span class="signup">Sign Up</span>
    <div class="envelope" role="img" aria-label="Airmail envelope"></div>
  </div>
</aside>

<footer class="site-footer abs"></footer>
<div class="contact-panel abs">
  <h4>CONTACT ME</h4>
  <div class="lead">I OFFER FREE CONSULTATIONS.</div>
  <p class="note single" style="top:58px">You can reach me by phone at <a href="#">(612) 555-0148</a>, or e-mail at <a href="#">Morgan@MorganValesLaw.com</a></p>
  <p class="note" style="top:77px">As you navigate the site, feel free at anytime to utilize the free services on the right to be connected through phone or e-mail automatically through the site.</p>
  <div class="attorney-photo" role="img" aria-label="Portrait of attorney Morgan Vales in a suit"></div>
</div>
<div class="talk-badge abs"><div class="name">Quick Talk</div><div class="num">+00 123 456 7890</div></div>
<div class="social abs" style="left:572px"><i></i>Circlebook</div>
<div class="social abs" style="left:646px"><i></i>Chirper</div>
<div class="copyright abs">© 2012 Law Offices of Morgan Vales PLLC</div>

<nav class="bottom-nav abs">
  <a href="#">CRIMINAL LAW</a><a href="#">FAMILY LAW</a><a href="#">WILL DRAFTING</a><a href="#">ATTORNEY PROFILE</a><a href="#">FEES</a><a href="#">LEGAL UPDATES</a><a href="#">ONLINE RESOURCES</a><a href="#">ARTICLES</a><a href="#">CONTACT</a>
</nav>

</body>
</html>
```